Tactical Supply Company needing memorable business card design

Our tactical supply comapny is in need of a new business card design that will set us apart from the amateurs. We sell tactical gear ranging from backpacks and range bags to apparel and other gear. We are looking for a sharp design that incorporates our logo, website, and name. Our colors are white, red, and black, or any combination of the three, preferably red and black.
I have attached our logo with our name underneath but I have also edited that design with the logo incorporated next to the name (attached).

Target Market(s)

Law enforcement, military, tactical

Industry/Entity Type

Business

Contact Information for Business Card

Include www.brindlequarry.example

Colors
000000
ec1f27
ffffff

Requirements
Must have
• Our name, logo, and website. This is intended to be a memorable simple card, no name, address, email, or phone number info is necessary. Designs that do include this additional info will still be considered if they are absolutely spectacular.
Should not have
• A standard template design, I can create that in my own on Cardomix. I am looking for a new, creative design that is completely unique to my company.

```html
<!DOCTYPE html>
<html lang="en">
<head>
<meta charset="utf-8">
<title>Brindle Quarry Tactical Supply – Business Card</title>
<link href="https://fonts.googleapis.com/css2?family=Russo+One&family=Montserrat:wght@500;600;700&display=swap" rel="stylesheet">
<style>
  :root {
    --black: #000000;
    --card-black: #0b0b0c;
    --red: #ec1f27;
    --deep-red: #8e0d12;
    --white: #ffffff;
    --silver: #c9cbce;
    --steel: #3a3c40;
    --backdrop: #d9d4cc;
  }
  * { box-sizing: border-box; margin: 0; padding: 0; }
  html, body { width: 1200px; height: 1000px; overflow: hidden; }
  body {
    background: var(--backdrop);
    display: flex;
    flex-direction: column;
    align-items: center;
    justify-content: space-evenly;
    font-family: "Montserrat", sans-serif;
  }
  .card {
    position: relative;
    width: 780px;
    height: 446px;
    background: linear-gradient(160deg, #1a1a1c 0%, var(--card-black) 55%, #050505 100%);
    overflow: hidden;
    box-shadow: 0 6px 18px rgba(0,0,0,.25);
  }
  .band {
    position: absolute;
    left: 0; right: 0;
    height: 46px;
    background: linear-gradient(180deg, var(--red), var(--deep-red));
  }
  .band--top { top: 0; }
  .band--bottom { bottom: 0; }
  .band::after {
    content: "";
    position: absolute;
    left: 0; right: 0;
    height: 3px;
    background: var(--deep-red);
  }
  .band--top::after { bottom: -9px; }
  .band--bottom::after { top: -9px; }

  /* back side */
  .card--back .brand {
    position: absolute;
    inset: 0;
    display: flex;
    flex-direction: column;
    align-items: center;
    justify-content: center;
    gap: 14px;
  }
  .brand-mark {
    width: 70px; height: 70px;
    border-radius: 50%;
    background: var(--red);
  }
  .brand-name {
    font-family: "Russo One", sans-serif;
    font-size: 54px;
    color: var(--white);
    letter-spacing: 2px;
    line-height: 1;
  }
  .brand-tag {
    font-weight: 600;
    font-size: 17px;
    letter-spacing: 9px;
    color: var(--silver);
  }

  /* front side */
  .card--front .decor {
    position: absolute;
    right: 40px;
    top: 64px;
    width: 300px;
    height: 318px;
  }
  .card--front .identity {
    position: absolute;
    left: 56px;
    top: 96px;
  }
  .card--front .brand-name { font-size: 40px; }
  .card--front .brand-tag { font-size: 13px; letter-spacing: 7px; margin-top: 8px; display: block; }
  .contact-list {
    position: absolute;
    left: 56px;
    top: 230px;
    list-style: none;
    display: flex;
    flex-direction: column;
    gap: 8px;
  }
  .contact-list li {
    display: flex;
    align-items: center;
    gap: 12px;
    font-weight: 600;
    font-size: 22px;
    color: var(--silver);
  }
  .contact-icon {
    width: 20px; height: 20px;
    background: var(--deep-red);
    flex: none;
  }
</style>
</head>
<body>
  <section class="card card--back" aria-label="Business card back">
    <div class="band band--top"></div>
    <div class="brand">
      <div class="brand-mark"></div>
      <div class="brand-name">BRINDLE QUARRY</div>
      <div class="brand-tag">TACTICAL SUPPLY</div>
    </div>
    <div class="band band--bottom"></div>
  </section>

  <section class="card card--front" aria-label="Business card front">
    <div class="band band--top"></div>
    <svg class="decor" viewBox="0 0 300 318" role="img" aria-label="Large faint brand emblem area">
      <defs>
        <linearGradient id="decorFill" x1="0" y1="0" x2="1" y2="1">
          <stop offset="0" stop-color="#2a2b2e"/>
          <stop offset="1" stop-color="#141416"/>
        </linearGradient>
      </defs>
      <rect x="0" y="0" width="300" height="318" fill="url(#decorFill)"/>
    </svg>
    <div class="identity">
      <div class="brand-name">BRINDLE QUARRY</div>
      <span class="brand-tag">TACTICAL SUPPLY</span>
    </div>
    <ul class="contact-list">
      <li><span class="contact-icon"></span>www.brindlequarry.example</li>
      <li><span class="contact-icon"></span>social.example/brindlequarry</li>
      <li><span class="contact-icon"></span>chirp.example/brindlequarry</li>
      <li><span class="contact-icon"></span>snaps.example/brindlequarrytactical</li>
    </ul>
    <div class="band band--bottom"></div>
  </section>
</body>
</html>
```